one side yoga classes, other side rental log cabin

I need a flyer to advertise yoga classes on a lake , and to describe the various styles of classes, and who they can benefit, Days Times .prices
Linked to it is a rental log cabin that can be rented privetly to families or Groups (8 max) www.staysbycalderbrook.com This also is rented to yoga teacher that would like to Hire Cabin and the Studio www.velinoretreat.co.uk or
for Holistic weekends.

Teacher

```html
<!DOCTYPE html>
<html lang="en">
<head>
<meta charset="utf-8">
<title>Velino Retreat – Lakeside Yoga Flyer</title>
<link rel="stylesheet" href="https://fonts.googleapis.com/css2?family=Oswald:wght@300;400&family=Open+Sans:ital,wght@0,400;1,400&family=Yellowtail&display=block">
<style>
  :root {
    --red: #e01f26;
    --red-deep: #b5121a;
    --charcoal: #2e2e30;
    --ink: #2a2a2a;
    --paper: #ffffff;
  }
  * { box-sizing: border-box; margin: 0; padding: 0; }
  html, body { width: 900px; height: 1200px; overflow: hidden; background: #ffffff; }
  .flyer {
    position: relative; width: 900px; height: 1200px; overflow: hidden;
    background: var(--paper);
    font-family: "Open Sans", Arial, sans-serif; color: var(--ink);
  }
  .script { font-family: "Yellowtail", "Brush Script MT", cursive; font-weight: 400; }
  .cabin-photo {
    position: absolute; left: 0; top: 0; width: 900px; height: 520px;
    background: linear-gradient(180deg, #cfe3f2 0%, #e6eef3 10%, #6d5a4a 16%, #a9794f 30%, #8a6a4d 48%, #7fa060 60%, #5f8a49 68%, #5d7d8f 74%, #7f9cab 100%);
  }
  .shapes { position: absolute; left: 0; top: 0; }
  .site-tag {
    position: absolute; left: 0; top: 44px; width: 374px; height: 37px;
    background: linear-gradient(90deg, var(--red-deep), var(--red));
    border-radius: 0 18px 18px 0;
    color: var(--paper); font-size: 20px; line-height: 37px; padding-left: 50px;
  }
  .brand {
    position: absolute; left: 250px; top: 384px; width: 290px; text-align: center;
    font-family: "Oswald", Arial, sans-serif; font-weight: 300; color: var(--ink);
  }
  .brand-name { font-size: 46px; letter-spacing: 6px; line-height: 46px; }
  .brand-sub { font-size: 12px; letter-spacing: 1px; text-align: right; padding-right: 40px; line-height: 14px; }
  .meditation-photo {
    position: absolute; left: 200px; top: 440px; width: 250px; height: 580px;
    background: radial-gradient(ellipse at 50% 25%, rgba(214,196,176,0.55) 0%, rgba(226,218,210,0.35) 35%, rgba(240,238,236,0) 70%);
  }
  .headline { font-family: "Oswald", Arial, sans-serif; font-weight: 300; color: var(--ink); }
  .headline-lead {
    position: absolute; left: 480px; top: 458px; width: 372px; text-align: right;
    font-size: 41px; line-height: 52px; letter-spacing: 0.4px; white-space: nowrap;
  }
  .headline-sub {
    position: absolute; left: 480px; top: 508px; width: 372px; text-align: right;
    font-size: 30px; line-height: 34px; letter-spacing: 2.6px; white-space: nowrap;
  }
  .headline-heart {
    position: absolute; left: 492px; top: 540px; font-size: 70px; line-height: 70px; color: var(--red);
  }
  .headline-place {
    position: absolute; left: 675px; top: 548px; width: 174px;
    border-top: 2px solid var(--ink); padding-top: 8px;
    font-size: 27px; line-height: 30px; letter-spacing: 1.6px; white-space: nowrap;
  }
  .section-tab {
    position: absolute; left: 0; top: 532px; width: 229px; height: 38px;
    background: linear-gradient(90deg, var(--red-deep), var(--red));
    border-radius: 0 19px 19px 0;
    color: var(--paper); font-size: 30px; line-height: 38px; padding-left: 44px;
  }
  .about-text {
    position: absolute; left: 46px; top: 583px; width: 430px;
    font-size: 15.5px; line-height: 20px; white-space: nowrap;
  }
  .timetable {
    position: absolute; left: 50px; top: 767px; width: 398px;
    border-collapse: collapse; font-size: 17px; table-layout: fixed;
  }
  .timetable td { border: 1.5px solid var(--ink); height: 48px; padding-left: 32px; }
  .timetable .class-time { width: 186px; }
  .timetable .class-name { font-family: "Oswald", Arial, sans-serif; font-weight: 300; font-size: 20px; padding-left: 50px; }
  .course-note {
    position: absolute; left: 50px; top: 924px; width: 398px; text-align: center;
    font-style: italic; font-size: 18px; line-height: 26px; letter-spacing: 0.5px;
  }
  .benefit-panel {
    position: absolute; left: 495px; top: 636px; width: 354px; height: 471px;
    border-radius: 42px 42px 0 0;
    background: linear-gradient(90deg, #1f1f21 0%, #555557 60%, #444446 100%);
  }
  .benefit-label {
    position: absolute; left: 66px; top: 12px; width: 211px; height: 42px;
    border-radius: 21px; background: var(--paper); border: 3px solid #cfcfcf;
    text-align: center; color: var(--red); font-size: 28px; line-height: 36px;
  }
  .benefit-list {
    position: absolute; left: 18px; top: 89px; width: 330px; list-style: none;
    color: var(--paper); font-size: 18px; line-height: 23px; white-space: nowrap;
  }
  .benefit-list li { position: relative; padding-left: 27px; margin-bottom: 4.5px; }
  .benefit-list li::before {
    content: ""; position: absolute; left: 4px; top: 8px; width: 9px; height: 9px;
    border-radius: 50%; background: var(--red);
  }
  .group-badge {
    position: absolute; left: 160px; top: 961px; width: 206px; height: 206px;
    border-radius: 50%; background: var(--charcoal); border: 7px solid var(--red);
    display: flex; flex-direction: column; align-items: center; justify-content: center;
    text-align: center;
  }
  .group-badge-top { color: var(--paper); font-size: 19px; line-height: 24px; }
  .group-badge-main { color: var(--paper); font-size: 30px; line-height: 34px; }
  .group-badge-cap { color: var(--red); font-size: 20px; line-height: 24px; }
</style>
</head>
<body>
<main class="flyer">
  <div class="cabin-photo" role="img" aria-label="Photograph of the timber lakeside log cabin with conservatory, deck and lawn beside the water"></div>

  <svg class="shapes" width="900" height="1200" viewBox="0 0 900 1200" aria-hidden="true">
    <path d="M0,430 C200,300 420,265 600,330 C730,378 820,430 900,475 L900,1200 L0,1200 Z" fill="#ffffff"/>
    <path d="M0,405 C200,275 420,238 600,305 C730,352 820,405 900,452 L900,475 C820,430 730,378 600,330 C420,265 200,300 0,430 Z" fill="#e01f26"/>
    <path d="M0,440 C200,312 420,278 600,342 C730,390 820,440 900,482" fill="none" stroke="#3a3a3c" stroke-width="5"/>
    <path d="M0,1025 C160,980 330,1020 480,1080 C620,1135 780,1120 900,1085" fill="none" stroke="#3a3a3c" stroke-width="10"/>
    <path d="M0,1045 C160,1000 330,1040 480,1100 C620,1152 780,1140 900,1105 L900,1200 L0,1200 Z" fill="#e01f26"/>
  </svg>

  <div class="site-tag">www.staysbycalderbrook.com</div>

  <div class="brand">
    <div class="brand-name">VELINO</div>
    <div class="brand-sub">Retreat</div>
  </div>

  <div class="meditation-photo" role="img" aria-label="Faded photograph of a woman meditating cross-legged in a white robe"></div>

  <h1 class="headline">
    <span class="headline-lead">A PEACEFUL &amp; TRANQUIL</span>
    <span class="headline-sub">LAKESIDE RETREAT IN THE</span>
    <span class="headline-heart script">Heart</span>
    <span class="headline-place">OF NORFLOK</span>
  </h1>

  <div class="section-tab script">About Us</div>
  <p class="about-text">Lumen Yoga is a graceful and potent form of yoga,<br>based on flowing movements, directed breathing<br>and visualisation. With its foundations set firmly in<br>ancient yogic tradition, Lumen works on body, mind<br>and spirit—improving strength and flexibility,<br>creating core stability, building a heightened feeling<br>of positivity, and deeply relaxing and rejuvenating<br>your whole being.</p>

  <table class="timetable">
    <tr><td class="class-time">8-9</td><td class="class-name">Hatha Yoga</td></tr>
    <tr><td class="class-time">10-11.15</td><td class="class-name">Lumen Yoga</td></tr>
    <tr><td class="class-time">19.00-20.00</td><td class="class-name">Hatha Yoga</td></tr>
  </table>
  <p class="course-note">*1 day &amp; Extended Courses</p>

  <section class="benefit-panel">
    <div class="benefit-label script">Benefit</div>
    <ul class="benefit-list">
      <li>72 % found Lumen Yoga reduced<br>back pain</li>
      <li>93 % experienced improved<br>spine flexibility</li>
      <li>86% enjoyed increased energy<br>levels</li>
      <li>89% experienced improved<br>breathing</li>
      <li>89% have reduced &amp; controlled<br>stress levels</li>
      <li>81% have greater self-<br>empowerment</li>
    </ul>
  </section>

  <div class="group-badge">
    <span class="group-badge-top">FAMILIES OR</span>
    <span class="group-badge-main">GROUPS</span>
    <span class="group-badge-cap">(8 MAX)</span>
  </div>
</main>
</body>
</html>
```